Webdesign für Steuerberaterin
Zielgruppe
Ich bin Steuerberaterin. Meine Zielgruppe sind sowohl Privatpersonen als auch Unternehmer sowie Männer und Frauen.
Aufgabenstellung
Bitte mein Logo und Foto mit berücksichtigen. Ich möchte keine Website, auf der alle 'Reiter' als eine Seite von oben nach unten durchlaufen. Sondern wirklich einzelne, voneinander getrennte Seiten.

```html
<!DOCTYPE html>
<html lang="de">
<head>
<meta charset="utf-8">
<title>Sabine Hortmann – Steuerberaterin</title>
<link href="https://fonts.googleapis.com/css2?family=Cabin:wght@400&family=Cormorant+Garamond:wght@500&family=Noto+Sans:wght@400;700&display=swap" rel="stylesheet">
<style>
  :root {
    --navy: #070d2b;
    --gold: #b3882c;
    --gold-band: #dcb83c;
    --text: #4a4a4a;
    --white: #ffffff;
    --portrait-light: #e9e9ec;
    --portrait-dark: #c9cacf;
  }
  * { margin: 0; padding: 0; box-sizing: border-box; }
  html, body { width: 1200px; height: 768px; overflow: hidden; background: var(--white); }
  .page { position: relative; width: 1200px; height: 768px; }
  .sidebar { position: absolute; left: 0; top: 0; width: 308px; height: 742px; background: var(--navy); }
  .main-nav { position: absolute; left: 80px; top: 182px; list-style: none; }
  .main-nav li { height: 44px; }
  .main-nav a { font-family: "Cabin", sans-serif; font-size: 14px; color: var(--gold); text-decoration: none; }
  .brand { position: absolute; left: 312px; top: 70px; width: 260px; text-align: center;
    font-family: "Cormorant Garamond", serif; font-weight: 500; font-size: 26px; color: var(--gold);
    display: flex; align-items: center; justify-content: center; gap: 10px; }
  .brand-dot { width: 12px; height: 12px; border-radius: 50%; background: var(--gold); }
  .portrait { position: absolute; left: 194px; top: 222px; width: 457px; height: 312px;
    background: radial-gradient(ellipse at 55% 45%, var(--white) 0%, var(--portrait-light) 45%, var(--portrait-dark) 100%); }
  .welcome { position: absolute; left: 693px; top: 176px; width: 475px; text-align: center; }
  .welcome-title { font-family: "Cormorant Garamond", serif; font-weight: 500; font-size: 25px; color: var(--gold);
    padding-bottom: 16px; border-bottom: 2px solid var(--gold-band); }
  .welcome-lead { margin-top: 30px; font-family: "Noto Sans", sans-serif; font-weight: 700; font-size: 13px; color: var(--text); }
  .welcome-text { margin-top: 18px; font-family: "Noto Sans", sans-serif; font-size: 12.5px; line-height: 17px; color: var(--text); }
  .welcome-text + .welcome-text { margin-top: 19px; }
  .site-footer { position: absolute; left: 0; top: 742px; width: 1200px; height: 26px; background: var(--gold-band);
    font-family: "Cabin", sans-serif; font-size: 13px; color: var(--navy); padding: 4px 0 0 80px; }
  .site-footer a { color: var(--navy); text-decoration: none; }
  .site-footer .sep { margin: 0 8px; }
</style>
</head>
<body>
<div class="page">
  <aside class="sidebar">
    <ul class="main-nav">
      <li><a href="#">Über mich</a></li>
      <li><a href="#">Leistungen</a></li>
      <li><a href="#">Kontakt</a></li>
    </ul>
  </aside>

  <div class="brand"><span class="brand-dot"></span>Sabine Hortmann</div>

  <div class="portrait" role="img" aria-label="Porträtfoto der Steuerberaterin vor heller Steinwand"></div>

  <section class="welcome">
    <h1 class="welcome-title">Schön, dass Sie da sind</h1>
    <p class="welcome-lead">Ich freue mich, dass Sie den Weg zu mir gefunden haben!</p>
    <p class="welcome-text">Sie sind bei mir genau richtig:<br>
      Egal, ob Sie Privatperson sind, die Ihre Einkommensteuer-Erklärung<br>
      in vertrauensvolle Hände geben möchte,<br>
      oder Unternehmer, der sich z.B. das „Rundum-Sorglos-Paket“<br>
      mit Buchführung, Jahresabschluss und Steuererklärungen wünscht.</p>
    <p class="welcome-text">Schauen Sie sich hier gerne um und melden Sie sich bei mir<br>
      – ich bin bei jedem steuerlichen Thema<br>
      gerne Ihr kompetenter und zuverlässiger Ansprechpartner.</p>
    <p class="welcome-text">Für mich ist es eine Selbstverständlichkeit,<br>
      dass ich auch nach mehr als 12 Jahren Berufserfahrung<br>
      durch permanente Fortbildungen immer auf dem aktuellsten Stand<br>
      der relevanten Gesetze und Verordnungen bin.<br>
      Nur so kann ich Sie bestmöglich beraten.</p>
  </section>

  <footer class="site-footer">
    <a href="#">Impressum</a><span class="sep">|</span><a href="#">Datenschutz</a>
  </footer>
</div>
</body>
</html>
```